General contractor/GM consaltant business card

I need a card for my contracting company in North Dakota, we build industrial buildings for the oil feild and oil feild related companies offices, shops, airplain hangars, airports ext. We have a familly atmosphere on the job and are very relational and personal.
Industry/Entity Type
Industrial
Contact Information for Business Card
Kestrelmoor Builders LLC.
Dwight T.Halvorsun
4736 Quillfern dr. Colorado Springs, CO. 80927
Cell# 406-555-8142
dwight@kestrelmoorbuilders.com

```html
<!DOCTYPE html>
<html lang="en">
<head>
<meta charset="utf-8">
<title>Kestrelmoor Builders LLC — Business Card</title>
<link rel="stylesheet" href="https://fonts.googleapis.com/css2?family=Arimo:wght@700&display=swap">
<style>
  :root {
    --card-blue: #0014ad;
    --edge-navy: #000a45;
    --paper-white: #ffffff;
    --wordmark-white: #ffffff;
    --glow-shadow: rgba(0, 4, 50, 0.7);
  }
  html, body {
    margin: 0;
    padding: 0;
    width: 1200px;
    height: 686px;
    overflow: hidden;
    background: var(--paper-white);
  }
  .card {
    position: relative;
    width: 1200px;
    height: 686px;
    background: var(--paper-white);
  }
  .card-field {
    position: absolute;
    left: 0;
    top: 0;
    width: 1200px;
    height: 587px;
    background: var(--card-blue);
    border-bottom: 4px solid var(--edge-navy);
    box-shadow: 0 1px 3px rgba(0, 0, 0, 0.35);
  }
  .company-name {
    position: absolute;
    left: 365px;
    top: 272px;
    margin: 0;
    font-family: "Arimo", Arial, sans-serif;
    font-weight: 700;
    font-size: 63px;
    line-height: 69px;
    letter-spacing: 0.12em;
    color: var(--wordmark-white);
    text-shadow: 0 0 18px var(--glow-shadow), 0 0 36px var(--glow-shadow);
    white-space: nowrap;
  }
  .company-name span {
    display: block;
  }
</style>
</head>
<body>
  <div class="card">
    <div class="card-field">
      <h1 class="company-name">
        <span>Kestrelmoor</span>
        <span>Builders LLC</span>
      </h1>
    </div>
  </div>
</body>
</html>
```